I would like to design a flyer that I can put on car windows, inside peoples mailboxes. This flyer is to display Crestline Athletics and Wellness is now Open. I would like this to be a Free One Week Pass! I would like to have the following information on the flyer.
1) My logo - CRESTLINE ATHLETICS AND WELLNESS (I will upload the logo)
2) Hours of operation - Mon - Fri "5am - 10pm" Sat/Sun "6am -6pm"
3) Membership $59.00 "No Initiation Fee" Month to Month Membership.
Class are free. The Classes are Yoga, Salsa Classes, Bootcamps, HITT, Sports Performance,
4) Personal Training
5) Message Therapy
6) Address: 2871 Havelmoor Commerce Dr. Suite 213
Chantilly, VA 20347
7) mail@crestlineaw-example.com
8) Free One Week Pass

```html
<!DOCTYPE html>
<html lang="en">
<head>
<meta charset="utf-8">
<title>Crestline Athletics and Wellness – Free One Week Pass</title>
<link rel="stylesheet" href="https://fonts.googleapis.com/css2?family=Open+Sans:wght@400;600&display=swap">
<style>
  :root {
    --brand-red: #e0302a;
    --ink: #3a3a3a;
    --ink-soft: #555555;
    --paper: #ffffff;
    --backdrop: #ffffff;
    --ring-grey: #4a4a4a;
    --strip: rgba(70, 70, 70, 0.72);
    --rule-grey: #c9c9c9;
  }
  html, body {
    margin: 0;
    width: 1200px;
    height: 1200px;
    overflow: hidden;
    background: var(--backdrop);
  }
  .flyer {
    position: absolute;
    left: 20px;
    top: 190px;
    width: 1160px;
    height: 820px;
    font-family: "Open Sans", sans-serif;
  }
  .flyer svg { display: block; }
  .paper { fill: var(--paper); }
  .band { fill: var(--brand-red); }
  .accent-arc { fill: none; stroke: var(--brand-red); stroke-width: 4; }
  .promo-strip { fill: var(--strip); }
  .headline { fill: var(--paper); font-size: 46px; font-weight: 400; }
  .rule-white { stroke: var(--paper); stroke-width: 4; }
  .rule-red { stroke: var(--brand-red); stroke-width: 4; }
  .perk { fill: var(--paper); font-size: 27px; font-weight: 400; }
  .tick { fill: none; stroke: var(--brand-red); stroke-width: 3; stroke-linecap: round; stroke-linejoin: round; }
  .photo-ring { fill: var(--paper); }
  .badge-outer { fill: var(--ring-grey); }
  .badge-gap { fill: var(--paper); }
  .badge-core { fill: var(--brand-red); }
  .badge-text { fill: var(--paper); text-anchor: middle; font-weight: 400; }
  .badge-small { font-size: 18px; }
  .badge-price { font-size: 74px; font-weight: 600; }
  .badge-note { font-size: 24px; }
  .brand-dot { fill: var(--brand-red); }
  .brand-name { fill: var(--brand-red); font-weight: 400; }
  .brand-main { font-size: 44px; }
  .brand-sub { font-size: 13.5px; letter-spacing: 2px; }
  .schedule-title { fill: var(--brand-red); font-size: 32px; font-weight: 400; }
  .schedule-rule { stroke: var(--rule-grey); stroke-width: 1; }
  .schedule-day { fill: var(--brand-red); font-size: 25px; }
  .schedule-hours { fill: var(--ink); font-size: 25px; }
  .classes { text-anchor: end; }
  .classes-lead { fill: var(--ink); font-size: 25px; font-weight: 600; }
  .classes-item { fill: var(--ink-soft); font-size: 19px; }
  .contact { fill: var(--paper); font-size: 24.5px; font-weight: 600; }
  .contact-mail { fill: var(--paper); font-size: 16px; font-weight: 600; }
</style>
</head>
<body>
<div class="flyer">
<svg width="1160" height="820" viewBox="0 0 1160 820" xmlns="http://www.w3.org/2000/svg">
  <defs>
    <linearGradient id="hero-tone" x1="0" y1="0" x2="1" y2="1">
      <stop offset="0" stop-color="#8a6a5a"/>
      <stop offset="0.45" stop-color="#b79a86"/>
      <stop offset="1" stop-color="#9c8374"/>
    </linearGradient>
    <linearGradient id="park-tone" x1="0" y1="0" x2="0" y2="1">
      <stop offset="0" stop-color="#7fae4a"/>
      <stop offset="1" stop-color="#4f9a36"/>
    </linearGradient>
    <radialGradient id="dance-tone" cx="0.5" cy="0.4" r="0.7">
      <stop offset="0" stop-color="#d99a4a"/>
      <stop offset="1" stop-color="#8a5420"/>
    </radialGradient>
    <linearGradient id="yoga-tone" x1="0" y1="0" x2="0" y2="1">
      <stop offset="0" stop-color="#c8b8aa"/>
      <stop offset="1" stop-color="#9a8c86"/>
    </linearGradient>
  </defs>

  <!-- paper -->
  <rect class="paper" x="0" y="0" width="1160" height="820"/>

  <!-- hero photo area -->
  <path role="img" aria-label="Photo: women lifting dumbbells overhead in a bright brick-walled studio"
        fill="url(#hero-tone)"
        d="M0,0 H720 C800,110 850,300 735,600 L700,665 H0 Z"/>
  <path class="accent-arc" d="M742,0 C820,110 872,300 760,590"/>

  <!-- promo strip -->
  <rect class="promo-strip" x="0" y="336" width="638" height="155"/>
  <text class="headline" x="346" y="402" text-anchor="middle">FREE ONE WEEK PASS</text>
  <line class="rule-white" x1="3" y1="416" x2="317" y2="416"/>
  <line class="rule-red" x1="317" y1="416" x2="641" y2="416"/>
  <path class="tick" d="M34,441 L40,450 L52,428"/>
  <text class="perk" x="60" y="450">PERSONAL TRAINING</text>
  <path class="tick" d="M358,441 L364,450 L376,428"/>
  <text class="perk" x="384" y="450">MESSAGE THERAPY</text>

  <!-- red footer band -->
  <rect class="band" x="0" y="665" width="1160" height="155"/>

  <!-- class photo circles -->
  <circle class="photo-ring" cx="762" cy="429" r="93"/>
  <circle role="img" aria-label="Photo: outdoor bootcamp group squatting on a lawn" fill="url(#park-tone)" cx="762" cy="429" r="88"/>
  <circle class="photo-ring" cx="637" cy="596" r="96"/>
  <circle role="img" aria-label="Photo: woman meditating in a yoga pose" fill="url(#yoga-tone)" cx="637" cy="596" r="90"/>
  <circle class="photo-ring" cx="436" cy="667" r="96"/>
  <circle role="img" aria-label="Photo: salsa dance couple" fill="url(#dance-tone)" cx="436" cy="667" r="90"/>

  <!-- membership badge -->
  <circle class="badge-outer" cx="187" cy="658" r="127"/>
  <circle class="badge-gap" cx="187" cy="658" r="120"/>
  <circle class="badge-core" cx="187" cy="658" r="115"/>
  <text class="badge-text badge-small" x="187" y="589">MEMBERSHIP</text>
  <text class="badge-text badge-price" x="187" y="662">$59</text>
  <text class="badge-text badge-note" x="187" y="686">"NO</text>
  <text class="badge-text badge-note" x="187" y="716">INITIATION</text>
  <text class="badge-text badge-note" x="187" y="746">FEE"</text>

  <!-- brand -->
  <circle class="brand-dot" cx="851" cy="86" r="44"/>
  <text class="brand-name brand-main" x="906" y="98">CRESTLINE</text>
  <text class="brand-name brand-sub" x="907" y="121">ATHLETICS AND WELLNESS</text>

  <!-- schedule -->
  <text class="schedule-title" x="862" y="245">TIME SCHEDULE</text>
  <line class="schedule-rule" x1="862" y1="258" x2="1056" y2="258"/>
  <text class="schedule-day" x="862" y="288">MON - FRI</text>
  <text class="schedule-hours" x="862" y="318">"5AM - 10PM"</text>
  <text class="schedule-day" x="862" y="367">SAT/SUN</text>
  <text class="schedule-hours" x="862" y="397">"6AM -6PM"</text>

  <!-- classes -->
  <g class="classes">
    <text class="classes-lead" x="1127" y="541">Class are free.</text>
    <text class="classes-item" x="1127" y="565">The Classes are Yoga</text>
    <text class="classes-item" x="1127" y="588">Salsa Classes</text>
    <text class="classes-item" x="1127" y="611">Bootcamps</text>
    <text class="classes-item" x="1127" y="634">HITT</text>
    <text class="classes-item" x="1127" y="657">Sports Performance</text>
  </g>

  <!-- contact -->
  <text class="contact" x="677" y="731">Address: 2871 Havelmoor Commerce Dr.</text>
  <text class="contact" x="677" y="761">Suite 213 Chantilly, VA 20347</text>
  <text class="contact-mail" x="677" y="784">mail@crestlineaw-example.com</text>
</svg>
</div>
</body>
</html>
```